KA VERLINE

We need a letterhead design for an Image & Etiquette Consultancy company based in Singapore.

The services we provide are Personal Image Consultation, Image & Etiquette Workshop for schools and corporate.

The design should have our corporate colour as seen in the logo files I have uploaded.

Since our company helps clients with their image, the design should be aesthetically very appealing. It should reflect a very classy & elegant feel.

I will print the letterhead using my printer but most of the time will use it to write letters to my clients therefore the format should include MS Word.

```html
<!DOCTYPE html>
<html lang="en">
<head>
<meta charset="utf-8">
<title>KA VERLINE — Letterhead</title>
<link rel="stylesheet" href="https://fonts.googleapis.com/css2?family=Questrial&family=Open+Sans:wght@400;600&display=swap">
<style>
  :root {
    --brand-purple: #2d0f4e;
    --brand-gold: #d6a62a;
    --text-grey: #6a6a6a;
    --page-white: #ffffff;
    --watermark-grey: #e6e6e8;
  }
  * { margin: 0; padding: 0; box-sizing: border-box; }
  html, body { width: 971px; height: 1200px; overflow: hidden; background: var(--page-white); }
  .letterhead {
    position: relative;
    width: 971px;
    height: 1200px;
    background: var(--page-white);
    font-family: "Questrial", "Century Gothic", sans-serif;
  }
  .top-band {
    position: absolute; top: 0; left: 0;
    width: 100%; height: 19px;
    background: var(--brand-purple);
  }
  .brand {
    position: absolute; left: 56px; top: 74px;
  }
  .brand-name {
    font-size: 68px;
    line-height: 1;
    letter-spacing: 2px;
    color: var(--brand-purple);
    font-weight: 400;
  }
  .brand-tagline {
    margin-top: 6px;
    font-size: 17.5px;
    letter-spacing: 1.8px;
    color: var(--brand-gold);
  }
  .contact {
    position: absolute; right: 53px; top: 52px;
    text-align: right;
    font-style: normal;
    color: var(--brand-purple);
  }
  .contact-title { font-size: 20px; letter-spacing: 1px; line-height: 1; margin-bottom: 10px; }
  .contact-address { font-size: 14.5px; color: var(--text-grey); margin-bottom: 7px; }
  .contact-phone { font-size: 20px; margin-bottom: 9px; }
  .contact-phone .value { color: var(--text-grey); }
  .contact-email, .contact-web {
    font-family: "Open Sans", "Tahoma", sans-serif;
    font-size: 14px;
    margin-bottom: 8px;
  }
  .contact-email .label { font-weight: 600; }
  .contact-email .value { color: var(--text-grey); }
  .contact-web { font-weight: 600; }
  .watermark {
    position: absolute; left: 0; right: 0; top: 1086px;
    text-align: center;
    font-size: 58px;
    letter-spacing: 1px;
    color: var(--watermark-grey);
  }
</style>
</head>
<body>
  <main class="letterhead">
    <div class="top-band"></div>

    <header class="brand">
      <div class="brand-name">KA VERLINE</div>
      <div class="brand-tagline">CONSULTANCY · Grace In Every Detail</div>
    </header>

    <address class="contact">
      <div class="contact-title">CONTACT US:</div>
      <div class="contact-address">Suite000, Cityname, Countryname</div>
      <div class="contact-phone">Phone: <span class="value">0198765432</span></div>
      <div class="contact-email"><span class="label">Email:</span> <span class="value">hello@kaverline.com</span></div>
      <div class="contact-web">www.kaverline.com</div>
    </address>

    <div class="watermark" aria-hidden="true">KA VERLINE</div>
  </main>
</body>
</html>
```